Attorney business card for two offices

Looking for a new business card design that can list both of my offices, one in Houston and one in West Texas. Want something masculine, easy to read, and conservative yet somewhat modern. Our current card has used a nautical star on it for years, but I am not necessarily attached to that. Also, a lot of our forms use dark green and orange. Second office address is P.O. Box 518, Dunmore, Texas 79615

```html
<!DOCTYPE html>
<html lang="en">
<head>
<meta charset="utf-8">
<title>The Hale Law Firm, P.C. – Business Card</title>
<link rel="stylesheet" href="https://fonts.googleapis.com/css2?family=Hind:wght@400;500;600&display=swap">
<style>
  :root {
    --green: #3b664c;
    --orange: #f5a21b;
    --white: #ffffff;
    --backdrop: #d6d6d6;
  }
  * { margin: 0; padding: 0; box-sizing: border-box; }
  html, body {
    width: 1038px;
    height: 1200px;
    overflow: hidden;
    background: var(--backdrop);
    font-family: "Hind", "Helvetica Neue", Arial, sans-serif;
  }
  .card {
    position: absolute;
    left: 70px;
    width: 897px;
    height: 518px;
    overflow: hidden;
  }
  .card-front { top: 41px; background: var(--green); }
  .card-back  { top: 622px; background: var(--white); }

  .brand-mark {
    position: absolute;
    left: 50%;
    top: 186px;
    width: 56px;
    height: 56px;
    margin-left: -28px;
    border-radius: 50%;
    background: var(--white);
  }
  .firm-name {
    position: absolute;
    left: 0; right: 0;
    top: 280px;
    text-align: center;
    color: var(--white);
    font-weight: 600;
    font-size: 36px;
    letter-spacing: 0.05em;
    line-height: 1;
  }

  .identity {
    position: absolute;
    left: 0; right: 0;
    top: 0;
    height: 248px;
    text-align: center;
    color: var(--green);
  }
  .attorney-name {
    position: absolute;
    left: 0; right: 0;
    top: 106px;
    font-weight: 600;
    font-size: 31px;
    letter-spacing: 0.06em;
    line-height: 1;
  }
  .attorney-title {
    position: absolute;
    left: 0; right: 0;
    top: 142px;
    font-weight: 400;
    font-size: 23px;
    letter-spacing: 0.08em;
    line-height: 1;
  }

  .contact-band {
    position: absolute;
    left: 0; right: 0;
    top: 248px;
    bottom: 0;
    background: var(--green);
    color: var(--white);
  }
  .office {
    position: absolute;
    top: 58px;
    width: 400px;
    text-align: center;
  }
  .office-houston { left: 34px; }
  .office-west    { left: 462px; }
  .office-label {
    color: var(--orange);
    font-weight: 600;
    font-size: 23px;
    letter-spacing: 0.05em;
    line-height: 28px;
  }
  .office-address {
    font-style: normal;
    font-size: 18px;
    letter-spacing: 0.06em;
    line-height: 30px;
    margin-top: 1px;
  }
  .office-west .office-address { font-variant: small-caps; }
  .office-divider {
    position: absolute;
    left: 463px;
    top: 54px;
    width: 4px;
    height: 96px;
    background: var(--orange);
  }
  .contact-line {
    position: absolute;
    left: 0; right: 0;
    top: 194px;
    text-align: center;
    font-size: 18px;
    letter-spacing: 0.05em;
    line-height: 24px;
  }
  .contact-item { margin: 0 11px; }
  .contact-key { color: var(--orange); font-weight: 600; }
</style>
</head>
<body>
  <section class="card card-front">
    <span class="brand-mark" aria-hidden="true"></span>
    <h1 class="firm-name">THE HALE LAW FIRM, P.C.</h1>
  </section>

  <section class="card card-back">
    <div class="identity">
      <h2 class="attorney-name">DANIEL R. HALE, SR.</h2>
      <p class="attorney-title">ATTORNEY AT LAW</p>
    </div>
    <div class="contact-band">
      <div class="office office-houston">
        <h3 class="office-label">HOUSTON</h3>
        <address class="office-address">4410 CEDAR BEND ROAD, SUITE 210<br>HOUSTON, TEXAS 77041</address>
      </div>
      <span class="office-divider" aria-hidden="true"></span>
      <div class="office office-west">
        <h3 class="office-label">WEST TEXAS</h3>
        <address class="office-address">P.O. Box 518, Dunmore,<br>Texas 79615</address>
      </div>
      <p class="contact-line">
        <span class="contact-item"><span class="contact-key">P:</span> (713) 555-0142</span>
        <span class="contact-item"><span class="contact-key">F:</span> (832) 555-0187</span>
        <span class="contact-item"><span class="contact-key">E:</span> DANIEL@HALETEXLAW.COM</span>
      </p>
    </div>
  </section>
</body>
</html>
```